Business Card Design

I need a Business Card that will catch the attention that will not get thrown in a Drawer. I have 23 companies I use for Auto, Home, Life, and Business Insurance. I make sure that people have the best coverage for the $ spent.

Industry/Entity Type

Business

Contact Information for Business Card

Torvin Insurance Agency, Inc., Derek Halloway, 4735 West Fallow Lane Ashcombe, Iowa 52913 555-287-6194, www.torvinagency-example.com, Kinnectly, Workweave, Circlewave

```html
<!DOCTYPE html>
<html lang="en">
<head>
<meta charset="utf-8">
<title>Torvin Insurance Agency – Business Card</title>
<link rel="stylesheet" href="https://fonts.googleapis.com/css2?family=Roboto+Condensed:wght@400&family=Tinos:wght@700&display=swap">
<style>
  :root {
    --paper: #ffffff;
    --umber: #50463d;
    --accent: #ee7a32;
    --ink: #111111;
    --light: #ffffff;
    --stripe: #cfc9c3;
  }
  html, body {
    margin: 0;
    padding: 0;
    width: 1200px;
    height: 702px;
    overflow: hidden;
    background: var(--paper);
  }
  .card {
    position: relative;
    width: 1200px;
    height: 702px;
    background: var(--paper);
    font-family: "Roboto Condensed", "Arial Narrow", sans-serif;
  }
  .card__face {
    position: absolute;
    left: 19px;
    top: 19px;
    width: 1162px;
    height: 665px;
    background: var(--umber);
    overflow: hidden;
  }
  .card__holder {
    position: absolute;
    left: 35px;
    top: 45px;
    margin: 0;
    font-size: 30px;
    font-weight: 400;
    color: var(--light);
  }
  .card__company {
    position: absolute;
    left: 0;
    right: 0;
    top: 174px;
    margin: 0;
    text-align: center;
    font-family: "Tinos", "Times New Roman", serif;
    font-weight: 700;
    font-size: 46px;
    color: var(--light);
    text-shadow: 3px 4px 5px rgba(0, 0, 0, 0.55);
  }
  .contact-panel {
    position: absolute;
    left: 0;
    top: 354px;
    width: 708px;
    height: 167px;
    background: var(--paper);
    border-radius: 0 28px 28px 0;
  }
  .side-tab {
    position: absolute;
    right: 0;
    top: 354px;
    width: 66px;
    height: 167px;
    background: var(--paper);
    border-radius: 28px 0 0 28px;
  }
  .contact-list, .social-list {
    list-style: none;
    margin: 0;
    padding: 0;
    position: absolute;
  }
  .contact-list { left: 18px; top: 364px; }
  .social-list { left: 792px; top: 364px; }
  .contact-list li, .social-list li {
    display: flex;
    align-items: center;
    height: 51px;
    font-size: 31px;
    letter-spacing: -0.2px;
  }
  .contact-list li { color: var(--ink); }
  .social-list li { color: var(--light); font-size: 30px; }
  .contact-list li:nth-child(3), .social-list li:nth-child(3) { height: 56px; }
  .icon {
    width: 44px;
    height: 44px;
    flex: none;
    margin-right: 14px;
  }
  .social-list .icon { margin-right: 20px; }
  .card__stripes {
    position: absolute;
    left: 0;
    right: 0;
    bottom: 3px;
    height: 44px;
    background: repeating-linear-gradient(to bottom, var(--stripe) 0 1px, var(--umber) 1px 3px);
  }
  .card__rule {
    position: absolute;
    left: 0;
    right: 0;
    bottom: 0;
    height: 3px;
    background: var(--accent);
  }
</style>
</head>
<body>
  <div class="card">
    <div class="card__face">
      <h2 class="card__holder">Derek Halloway</h2>
      <h1 class="card__company">Torvin Insurance Agency, Inc.</h1>

      <div class="contact-panel"></div>
      <div class="side-tab"></div>

      <ul class="contact-list">
        <li>
          <svg class="icon" viewBox="0 0 44 44" aria-hidden="true">
            <circle cx="22" cy="22" r="20" fill="var(--accent)"/>
            <path d="M12 17c0-3 4-5 10-5s10 2 10 5v2h-5v-3h-10v3h-5z" fill="#fff"/>
            <rect x="13" y="21" width="18" height="11" rx="2" fill="#fff"/>
            <circle cx="22" cy="26.5" r="3" fill="var(--accent)"/>
          </svg>
          <span>555-287-6194</span>
        </li>
        <li>
          <svg class="icon" viewBox="0 0 44 44" aria-hidden="true">
            <circle cx="22" cy="22" r="19.5" fill="#fff" stroke="var(--accent)" stroke-width="2.5"/>
            <g fill="none" stroke="var(--accent)" stroke-width="1.8">
              <circle cx="22" cy="22" r="11"/>
              <ellipse cx="22" cy="22" rx="5" ry="11"/>
              <line x1="11" y1="22" x2="33" y2="22"/>
              <line x1="22" y1="11" x2="22" y2="33"/>
              <path d="M13 16h18M13 28h18"/>
            </g>
          </svg>
          <span>www.torvinagency-example.com</span>
        </li>
        <li>
          <svg class="icon" viewBox="0 0 44 44" aria-hidden="true">
            <circle cx="22" cy="22" r="19.5" fill="#fff" stroke="var(--accent)" stroke-width="2.5"/>
            <path d="M22 34c-5-7-8-11-8-15a8 8 0 0 1 16 0c0 4-3 8-8 15z" fill="var(--accent)"/>
            <circle cx="22" cy="19" r="3" fill="#fff"/>
          </svg>
          <span>4735 West Fallow Lane Ashcombe, Iowa 52913</span>
        </li>
      </ul>

      <ul class="social-list">
        <li>
          <svg class="icon" viewBox="0 0 44 44" aria-hidden="true">
            <circle cx="22" cy="22" r="19.5" fill="#fff" stroke="var(--accent)" stroke-width="2.5"/>
          </svg>
          <span>Kinnectly</span>
        </li>
        <li>
          <svg class="icon" viewBox="0 0 44 44" aria-hidden="true">
            <circle cx="22" cy="22" r="19.5" fill="#fff" stroke="var(--accent)" stroke-width="2.5"/>
          </svg>
          <span>Circlewave</span>
        </li>
        <li>
          <svg class="icon" viewBox="0 0 44 44" aria-hidden="true">
            <circle cx="22" cy="22" r="19.5" fill="#fff" stroke="var(--accent)" stroke-width="2.5"/>
          </svg>
          <span>Workweave</span>
        </li>
      </ul>

      <div class="card__stripes"></div>
      <div class="card__rule"></div>
    </div>
  </div>
</body>
</html>
```